Skip Bin Hire Business

We are an existing business that hire out skip bins for domestic and commercial use. We are looking for a fresh look with no colours or designs in mind.
We have 2m3 and 3m3 skip bins and 3m3 up to 24m3 walk in bins.
Visit our website for more information.
www.harborcrate.com.au
We are going to add a photo of a 3m3 skip as this is a new product for our company and not available on our website at this stage.

Industry/Entity Type

Business

Contact Information for Business Card

Harbor Crate
9172-4086
www.harborcrate.com.au

```html
<!DOCTYPE html>
<html lang="en">
<head>
<meta charset="utf-8">
<title>Harbor Crate – Business Card</title>
<link href="https://fonts.googleapis.com/css2?family=Open+Sans:wght@400;600;800&display=swap" rel="stylesheet">
<style>
  :root {
    --card-yellow: #f7ab22;
    --ink: #2a2a2a;
    --badge-text: #ffffff;
    --backdrop: #e9e9e9;
  }
  html, body {
    margin: 0;
    padding: 0;
    width: 1200px;
    height: 1000px;
    overflow: hidden;
    background: var(--backdrop);
  }
  .canvas {
    position: relative;
    width: 1200px;
    height: 1000px;
  }
  .business-card {
    position: absolute;
    left: 150px;
    top: 243px;
    width: 900px;
    height: 514px;
    background: var(--card-yellow);
    font-family: "Open Sans", Arial, sans-serif;
    color: var(--ink);
    box-shadow: 0 12px 30px rgba(0,0,0,0.18);
    overflow: hidden;
  }
  .brand-name {
    position: absolute;
    left: 300px;
    top: 92px;
    margin: 0;
    font-size: 82px;
    font-weight: 600;
    letter-spacing: 1px;
    line-height: 1;
    white-space: nowrap;
  }
  .phone-rule {
    position: absolute;
    height: 4px;
    background: var(--ink);
  }
  .phone-rule.upper { left: 330px; top: 222px; width: 300px; }
  .phone-rule.lower { left: 300px; top: 302px; width: 300px; }
  .phone {
    position: absolute;
    left: 318px;
    top: 236px;
    margin: 0;
    font-size: 40px;
    font-weight: 400;
    line-height: 1.2;
    white-space: nowrap;
  }
  .booking-line {
    position: absolute;
    left: 0;
    top: 0;
  }
  .book-badge {
    position: absolute;
    left: 58px;
    top: 385px;
    width: 150px;
    height: 74px;
    border-radius: 30px;
    background: var(--ink);
    color: var(--badge-text);
    font-weight: 800;
    font-size: 22px;
    line-height: 1;
    letter-spacing: 1px;
    display: flex;
    flex-direction: column;
    align-items: center;
    justify-content: center;
    gap: 2px;
  }
  .website {
    position: absolute;
    left: 235px;
    top: 372px;
    margin: 0;
    font-size: 26px;
    font-weight: 400;
    letter-spacing: 4px;
    white-space: nowrap;
  }
</style>
</head>
<body>
  <main class="canvas">
    <section class="business-card" aria-label="Harbor Crate business card">
      <h1 class="brand-name">Harbor Crate</h1>
      <span class="phone-rule upper"></span>
      <p class="phone">Ph: 9172-4086</p>
      <span class="phone-rule lower"></span>

      <svg class="booking-line" width="900" height="514" viewBox="0 0 900 514" aria-hidden="true">
        <line x1="0" y1="422" x2="820" y2="422" stroke="#2a2a2a" stroke-width="4"/>
        <circle cx="822" cy="422" r="8" fill="#2a2a2a"/>
      </svg>

      <div class="book-badge"><span>BOOK</span><span>ONLINE</span></div>
      <p class="website">www.harborcrate.com.au</p>
    </section>
  </main>
</body>
</html>
```